Nexor Turbo Business Card Design

This is a start up company that has state of the art patented technology for turbo chargers,that can be used on engines, gas or diesel, for any type of automotive,aviation,marine or industrial purpose.
This technology will provide longer life,lower maintenance and better performance and help produce lower emissions with any turbocharged engine.Red would be a predominate color and the design should communicate the latest technology,economy and
Environmental concern.
This product will initially be distributed in the U.S.A. But should move rapidly to global use.
Updates

Thank you for your design submissions, I have increased the budget for this job because my initial order was too low for the quality of work shown, plus I would Like to see some more options. I have a meeting this Sunday with my other partners and would anticipate being able to give you some feedback by the Beginning of next week. Regards.

Thank you for everyone's participation. The deadline is still open until 6/15 and my partners and I have a meeting Scheduled this weekend. At this time we have not ruled anyone out, But will be making a decision during the course of our meeting and wil Decide which direction we will be going in by the beginning of the week. Thanks again, regards, Dan Ferris.

Hello everybody, Sorry for the delay in communication, we have been very busy in putting the start up together. We are still not decided on the design of the business card and have a wide range to choose from. I would anticipated we shall have an answer within the next two weeks. Regards, Dan Ferris.

Target Market(s)

Manufacturers and wholesalers' of OEM and replacement turbochargers

Industry/Entity Type

Industrial

Contact Information for Business Card

We need a logo that should incorporate the " Nexor, a " possibly super imposed over a turbo charger with the fan blades of the turbocharger showing in the center of the "a" .
Name,title,phone number and email address only, no street/mailing address at this time.
The full name of the company is
" Nexor Turbo Technologies LLC "
For the initial card you can use my info.
Daniel Ferris
VP Sales & Marketing
dferris@nexorturbotechnologies.com
555 014 2876

Requirements
Must have
• The Nexor A, the outline of a turbo charger
Nice to have
• Something classy and simple and worldly (global)
Should not have
• No engines,cars,boats,planes

```html
<!DOCTYPE html>
<html lang="en">
<head>
<meta charset="utf-8">
<title>Nexor Turbo Technologies LLC — Business Card</title>
<link rel="stylesheet" href="https://fonts.googleapis.com/css2?family=Federo&display=swap">
<style>
  :root {
    --card-red: #ff0000;
    --ink-white: #ffffff;
    --turbo-dark: #2a0000;
    --turbo-mid: #8a0000;
  }
  html, body {
    margin: 0;
    padding: 0;
    width: 1200px;
    height: 664px;
    overflow: hidden;
    background: var(--card-red);
  }
  .card {
    position: relative;
    width: 1200px;
    height: 664px;
    background: var(--card-red);
    color: var(--ink-white);
    font-family: "Federo", sans-serif;
    font-weight: 400;
    overflow: hidden;
  }
  .card p, .card h1 { margin: 0; font-weight: 400; white-space: nowrap; }

  .company-name {
    position: absolute;
    left: 0;
    top: 14px;
    width: 1200px;
    text-align: center;
    font-size: 74px;
    line-height: 96px;
    letter-spacing: 3px;
  }

  .turbo-artwork {
    position: absolute;
    left: 30px;
    top: 85px;
    width: 580px;
    height: 570px;
    border-radius: 48% 52% 50% 50%;
    background: radial-gradient(ellipse at 58% 50%,
      var(--turbo-dark) 0%,
      var(--turbo-dark) 22%,
      var(--turbo-mid) 48%,
      rgba(255, 0, 0, 0) 72%);
  }

  .brand-mark {
    position: absolute;
    left: 270px;
    top: 325px;
    width: 200px;
    height: 60px;
    display: flex;
    align-items: center;
    justify-content: center;
    gap: 10px;
    font-size: 40px;
    color: var(--ink-white);
  }
  .brand-mark .dot {
    width: 16px;
    height: 16px;
    border-radius: 50%;
    background: var(--card-red);
  }

  .person {
    position: absolute;
    left: 520px;
    top: 244px;
    width: 600px;
    text-align: center;
    font-size: 48px;
    line-height: 56px;
  }
  .person-name { padding-left: 0; }

  .contact-phone {
    position: absolute;
    left: 618px;
    top: 518px;
    width: 400px;
    text-align: center;
    font-size: 38px;
    line-height: 52px;
    letter-spacing: 2px;
  }
  .contact-email {
    position: absolute;
    right: 40px;
    top: 572px;
    font-size: 35px;
    line-height: 52px;
    letter-spacing: 0.5px;
  }
</style>
</head>
<body>
  <main class="card">
    <h1 class="company-name">Nexor Turbo Technologies LLC</h1>

    <div class="turbo-artwork" role="img" aria-label="Stylised turbocharger illustration in black and red"></div>
    <div class="brand-mark"><span class="dot"></span>Nexor</div>

    <section class="person">
      <p class="person-name">Daniel Ferris</p>
      <p class="person-title">VP Sales &amp; Marketing</p>
    </section>

    <p class="contact-phone">555 014 2876</p>
    <p class="contact-email">dferris@nexorturbotechnologies.com</p>
  </main>
</body>
</html>
```